Gaphic explaining connectivity of research areas that use DNA analysis

We are a university research group in Perth Western Australia focused on ecology and environment fields. Our work can be explained by three broad areas where its applied - what used to be present ('ancient DNA analysis'), what is present now ('environmental DNA analysis') and what happened in terms of DNA based changes in between ('genomic changes'). To help simply convey this to other researchers and importantly non-science-savvy people we wanted an a eye catching rework of the attached for our website, future presentations, brochures etc. We didn't want it too visually complicated, nor wordy so something akin to the attached with a better look will help . More background on each point can be read on the website under construction here - https://natsci.belvane.edu.au/plimb-lab/

Target Market(s)

other science researchers in ecology, environment, geology, forensics areas, although ultimately its meant to be a simple way to understand for all people

Font styles to use
Sans Serif

Requirements
Must have
• the three areas indicated
Should not have
• design does not need to follow the colour pallet of the university (ie poo brown and black)

```html
<!DOCTYPE html>
<html lang="en">
<head>
<meta charset="utf-8">
<title>Connectivity of Research Areas That Use DNA Analysis</title>
<link rel="stylesheet" href="https://fonts.googleapis.com/css2?family=Montserrat:wght@500;600;700&display=swap">
<style>
  :root {
    --ink: #212322;
    --gold: #c69100;
    --paper: #ffffff;
  }
  html, body {
    margin: 0;
    padding: 0;
    width: 1200px;
    height: 800px;
    overflow: hidden;
    background: var(--paper);
  }
  .canvas {
    display: block;
    width: 1200px;
    height: 800px;
    font-family: "Montserrat", Arial, sans-serif;
  }
  .title { fill: var(--ink); font-size: 30px; font-weight: 700; }
  .area-label { fill: var(--paper); font-size: 21px; font-weight: 500; }
  .question { fill: var(--ink); font-size: 23px; font-weight: 500; }
  .question--accent { fill: var(--gold); }
  .summary { fill: var(--ink); font-size: 19px; font-weight: 700; }
  .brand-name { fill: var(--ink); font-size: 26px; font-weight: 500; }
  .thread { fill: none; stroke: var(--ink); stroke-width: 1.6; }
  .stem { stroke: var(--ink); stroke-width: 2; }
  .ring--gold { fill: var(--paper); stroke: var(--gold); stroke-width: 14; }
  .ring--ink { fill: var(--paper); stroke: var(--ink); stroke-width: 14; }
  .icon { fill: none; stroke: var(--ink); stroke-width: 3; stroke-linecap: round; stroke-linejoin: round; }
  .band--ink { fill: var(--ink); }
  .band--gold { fill: var(--gold); }
  .brand-mark { fill: var(--gold); }
</style>
</head>
<body>
<svg class="canvas" viewBox="0 0 1200 800" xmlns="http://www.w3.org/2000/svg" role="img" aria-label="Connectivity of research areas that use DNA analysis: aDNA, genomic and eDNA">
  <defs>
    <g id="helix">
      <path d="M2 0 C2 10 30 11 30 21 C30 31 2 33 2 43 C2 53 30 54 30 64"/>
      <path d="M30 0 C30 10 2 11 2 21 C2 31 30 33 30 43 C30 53 2 54 2 64"/>
      <line x1="9" y1="2" x2="23" y2="2"/>
      <line x1="13" y1="9" x2="19" y2="9"/>
      <line x1="9" y1="27" x2="23" y2="27"/>
      <line x1="9" y1="36" x2="23" y2="36"/>
      <line x1="13" y1="55" x2="19" y2="55"/>
      <line x1="9" y1="62" x2="23" y2="62"/>
    </g>
  </defs>

  <!-- Heading -->
  <text class="title" x="600" y="123" text-anchor="middle" textLength="764" lengthAdjust="spacing">CONNECTIVITY OF RESEARCH AREAS</text>
  <text class="title" x="600" y="160" text-anchor="middle" textLength="520" lengthAdjust="spacing">THAT USE DNA ANALYSIS</text>

  <!-- Connecting thread -->
  <path class="thread" d="M255 297 A96 96 0 0 0 449 297 A29 29 0 0 1 507 297 A98 98 0 0 0 703 297 A28.5 28.5 0 0 1 760 297 A98 98 0 0 0 955 297"/>
  <circle cx="255" cy="297" r="3.5" fill="var(--ink)"/>
  <circle cx="955" cy="297" r="3.5" fill="var(--ink)"/>

  <!-- Stems to band -->
  <line class="stem" x1="352" y1="392" x2="352" y2="434"/>
  <line class="stem" x1="605" y1="392" x2="605" y2="434"/>
  <line class="stem" x1="858" y1="392" x2="858" y2="434"/>

  <!-- Area rings -->
  <circle class="ring--gold" cx="351" cy="294" r="79"/>
  <circle class="ring--ink" cx="605" cy="294" r="79"/>
  <circle class="ring--gold" cx="858" cy="294" r="79"/>

  <!-- aDNA icon: helix with magnifier -->
  <g class="icon" transform="translate(351 294)">
    <g transform="rotate(45) translate(-14 -40) scale(0.9 1.25)">
      <use href="#helix"/>
    </g>
    <circle cx="13" cy="10" r="16" fill="var(--paper)"/>
    <line x1="25" y1="22" x2="37" y2="34"/>
    <circle cx="9" cy="7" r="2.5"/>
    <circle cx="15" cy="1" r="1"/>
    <circle cx="3" cy="12" r="1"/>
  </g>

  <!-- Genomic icon: two helices with exchange arrows -->
  <g class="icon">
    <use href="#helix" x="559" y="262"/>
    <use href="#helix" x="620" y="262"/>
    <line x1="595" y1="280" x2="615" y2="280"/>
    <path d="M599 276 L595 280 L599 284 M611 276 L615 280 L611 284"/>
    <line x1="595" y1="308" x2="615" y2="308"/>
    <path d="M599 304 L595 308 L599 312 M611 304 L615 308 L611 312"/>
  </g>

  <!-- eDNA icon: helix in cycle arrows -->
  <g class="icon">
    <use href="#helix" x="843" y="264"/>
    <path d="M815 284 A44 44 0 0 1 900 282"/>
    <path d="M807 274 L814 285 L825 279"/>
    <path d="M815 306 A44 44 0 0 0 900 306"/>
    <path d="M890 310 L902 303 L908 314"/>
  </g>

  <!-- Area band -->
  <path class="band--ink" d="M251 433 H474 V471 H251 A19 19 0 0 1 251 433 Z"/>
  <rect class="band--gold" x="473" y="433" width="265" height="38"/>
  <path class="band--ink" d="M737 433 H959 A19 19 0 0 1 959 471 H737 Z"/>
  <text class="area-label" x="346" y="460" text-anchor="middle" letter-spacing="6">aDNA</text>
  <text class="area-label" x="605" y="460" text-anchor="middle" letter-spacing="6">GENOMIC</text>
  <text class="area-label" x="856" y="460" text-anchor="middle" letter-spacing="6">eDNA</text>

  <!-- Guiding questions -->
  <text class="question" x="351" y="503" text-anchor="middle" textLength="202" lengthAdjust="spacing">What used to</text>
  <text class="question" x="352" y="530" text-anchor="middle" textLength="178" lengthAdjust="spacing">be present?</text>
  <text class="question question--accent" x="605" y="503" text-anchor="middle" textLength="236" lengthAdjust="spacing">What happened</text>
  <text class="question question--accent" x="606" y="530" text-anchor="middle" textLength="231" lengthAdjust="spacing">along the way?</text>
  <text class="question" x="855" y="503" text-anchor="middle" textLength="112" lengthAdjust="spacing">What is</text>
  <text class="question" x="855" y="530" text-anchor="middle" textLength="131" lengthAdjust="spacing">present?</text>

  <!-- Leads to summary -->
  <line class="stem" x1="352" y1="540" x2="352" y2="606"/>
  <line class="stem" x1="605" y1="540" x2="605" y2="606"/>
  <line class="stem" x1="858" y1="540" x2="858" y2="606"/>

  <!-- Summary -->
  <text class="summary" x="604" y="644" text-anchor="middle" textLength="880" lengthAdjust="spacing">INSIGHT ON THE FORMATION, DISTRIBUTION, AND RESILIENCE</text>
  <text class="summary" x="604" y="668" text-anchor="middle" textLength="428" lengthAdjust="spacing">OF AUSTRALIAN BIODIVERSITY</text>

  <!-- Institution name -->
  <rect class="brand-mark" x="908" y="743" width="47" height="46"/>
  <text class="brand-name" x="967" y="775" textLength="210" lengthAdjust="spacingAndGlyphs">Belvane University</text>
</svg>
</body>
</html>
```